Steadfast MD - Sleep Medicine Specialist - Business Cards

We are a new medical practice called Steadfast MD. We are sleep medicine specialists and we will be conducting sleep studies on patients with sleep related ailments. We want the business card to be bold, professional, and clean with the logo as the stand out visual piece. We dont like wild flashy designs. We want our design to be bold and classic while at the same time conveying who we are and what we do. We are reliable, professional, and the best in the business.

Industry/Entity Type

Health Care

Contact Information for Business Card

- Clean
- Bold
- Classic
- not cluttered

Requirements
Must have
• logo, website, phone number
Nice to have
• several options to choose from
Should not have
• flashy imaged - reflective print - images of people sleeping

```html
<!DOCTYPE html>
<html lang="en">
<head>
<meta charset="utf-8">
<title>Steadfast MD – Business Card</title>
<link href="https://fonts.googleapis.com/css2?family=Arimo:wght@400;700&display=swap" rel="stylesheet">
<style>
  :root {
    --backdrop: #e4e4e4;
    --card-dark: #060708;
    --card-light: #f4f4f4;
    --brand-red: #e0202a;
    --ink: #111111;
    --ring-dark: #1f2022;
    --ring-light: #f2d9d9;
  }
  * { margin: 0; padding: 0; box-sizing: border-box; }
  html, body {
    width: 1200px; height: 960px; overflow: hidden;
    background: var(--backdrop);
    font-family: "Arimo", Arial, sans-serif;
  }
  .stage { position: relative; width: 1200px; height: 960px; }
  .card {
    position: absolute; left: 297px; width: 606px; height: 347px; overflow: hidden;
  }
  .card--front { top: 113px; background: var(--card-dark); }
  .card--back { top: 513px; background: var(--card-light); }
  .card__ring { position: absolute; inset: 0; }
  .brand { position: absolute; display: flex; align-items: center; }
  .brand__dot { flex: none; border-radius: 50%; border-style: solid; border-color: var(--brand-red); }
  .brand__name { font-weight: 700; letter-spacing: -0.5px; white-space: nowrap; }
  .card--front .brand { left: 135px; top: 131px; gap: 7px; }
  .card--front .brand__dot { width: 86px; height: 86px; border-width: 3px; }
  .card--front .brand__name { font-size: 40px; color: #ffffff; }
  .card--back .brand { left: 53px; top: 45px; gap: 6px; }
  .card--back .brand__dot { width: 67px; height: 67px; border-width: 2.5px; }
  .card--back .brand__name { font-size: 30px; color: var(--ink); }
  .edge-bar { position: absolute; left: 0; top: 0; width: 14px; height: 100%; background: var(--ink); }
  .edge-bar__accent { position: absolute; left: 0; top: 175px; width: 14px; height: 43px; background: var(--brand-red); }
  .person { position: absolute; left: 53px; top: 174px; }
  .person__name { font-size: 20px; font-weight: 700; color: var(--brand-red); letter-spacing: 0.2px; }
  .person__role { font-size: 15px; color: var(--ink); margin-top: 3px; }
  .contacts { position: absolute; left: 53px; top: 246px; list-style: none; }
  .contacts li { display: flex; align-items: center; gap: 6px; font-size: 15px; color: var(--ink); height: 20px; }
  .contacts svg { width: 13px; height: 13px; flex: none; }
</style>
</head>
<body>
<main class="stage">
  <section class="card card--front">
    <svg class="card__ring" viewBox="0 0 606 347" aria-hidden="true">
      <circle cx="515" cy="174" r="168" fill="none" stroke="var(--ring-dark)" stroke-width="10"/>
    </svg>
    <div class="brand">
      <span class="brand__dot"></span>
      <span class="brand__name">Steadfast MD</span>
    </div>
  </section>

  <section class="card card--back">
    <svg class="card__ring" viewBox="0 0 606 347" aria-hidden="true">
      <circle cx="512" cy="256" r="152" fill="none" stroke="var(--ring-light)" stroke-width="6"/>
    </svg>
    <div class="edge-bar"><div class="edge-bar__accent"></div></div>
    <div class="brand">
      <span class="brand__dot"></span>
      <span class="brand__name">Steadfast MD</span>
    </div>
    <div class="person">
      <p class="person__name">DANIEL CARTER</p>
      <p class="person__role">Managing Director</p>
    </div>
    <ul class="contacts">
      <li>
        <svg viewBox="0 0 24 24" aria-hidden="true"><path fill="var(--brand-red)" d="M6.6 10.8a15.2 15.2 0 0 0 6.6 6.6l2.2-2.2c.3-.3.7-.4 1-.2 1.1.4 2.3.6 3.6.6.6 0 1 .4 1 1V20c0 .6-.4 1-1 1A17 17 0 0 1 3 4c0-.6.4-1 1-1h3.5c.6 0 1 .4 1 1 0 1.3.2 2.5.6 3.6.1.3 0 .7-.2 1z"/></svg>
        <span>(555) 014-2290</span>
      </li>
      <li>
        <svg viewBox="0 0 24 24" aria-hidden="true"><rect x="2.5" y="5" width="19" height="14" fill="none" stroke="var(--brand-red)" stroke-width="2.4"/><path d="M3 6l9 7 9-7" fill="none" stroke="var(--brand-red)" stroke-width="2.4"/></svg>
        <span>daniel@steadfastmd.com</span>
      </li>
      <li>
        <svg viewBox="0 0 24 24" aria-hidden="true"><circle cx="12" cy="12" r="9.5" fill="none" stroke="var(--brand-red)" stroke-width="2.2"/><path d="M2.5 12h19M12 2.5c3 3 3 16 0 19M12 2.5c-3 3-3 16 0 19" fill="none" stroke="var(--brand-red)" stroke-width="1.8"/></svg>
        <span>www.steadfastmd.com</span>
      </li>
    </ul>
  </section>
</main>
</body>
</html>
```